Trade Show Display Design For A Real Estate Lending Company

We are in need of an impactful and modern trade show booth design that is consistent with the new branding and imagery found on our website www.qvt7.net.

Established in 2010, Crestmoor Funding Partners, LLC is a Hard Money Lender providing fast bridge financing to real estate investors for the purchase, renovation, or new construction of single family, multi-family and mixed use properties. We have closed over 800 loans since we began with total transaction amounts in excess of $170 million.

We like to stress that we are local lenders, and our lending area includes NJ, NY, CT, MA, PA, FL, MD, VA, DC. In addition, one of our major differentiators is that we close loans extremely fast.
Here is what we need for this project, and the artwork templates are attached.

-1 backdrop display design
-1 countertop wrap design
-1 retractable banner design

The backdrop display and the countertop will be used together. The retractable banner will be used together with the backdrop and by itself.

Target Market(s)

Real estate agents, mortgage brokers, builders, and other real estate investors.

Industry/Entity Type

Real Estate

Font styles to use
Other font styles liked:
• Proxima Nova and Roboto Slab (or similar)

Requirements
Must have
• Must include a design for all three elements (backdrop, retractable banner, counter top). Final submission must also be submitted using the print-ready art templates provided.

```html
<!DOCTYPE html>
<html lang="en">
<head>
<meta charset="utf-8">
<title>Crestmoor Funding Partners – Trade Show Display</title>
<link href="https://fonts.googleapis.com/css2?family=Montserrat:wght@500;600;700&display=swap" rel="stylesheet">
<style>
:root{
  --teal:#5a9785;
  --teal-soft:rgba(90,151,133,.88);
  --navy:#0b4f63;
  --navy-soft:rgba(11,79,99,.9);
  --orange:#e39a2b;
  --ink:#444;
  --white:#fff;
}
*{box-sizing:border-box;margin:0;padding:0}
html,body{width:1029px;height:1200px;overflow:hidden;background:var(--white)}
body{position:relative;font-family:"Montserrat",sans-serif;color:var(--white)}
.abs{position:absolute}
.label{position:absolute;color:var(--ink);font-size:15px;font-weight:500;font-family:"Montserrat",sans-serif}

.brand{display:flex;align-items:center;gap:10px}
.brand-mark{background:var(--white);flex:none}
.brand-name{font-weight:700;line-height:1.15;color:var(--white);text-transform:uppercase}

/* Backdrop */
.backdrop{left:17px;top:21px;width:994px;height:568px;box-shadow:0 1px 3px rgba(0,0,0,.3);overflow:hidden}
.photo{position:absolute}
.photo-handshake{left:146px;top:0;width:337px;height:568px;background:linear-gradient(160deg,#a17a58,#7a5a42 45%,#c9cfd6 70%,#5b4838)}
.photo-family{left:486px;top:0;width:508px;height:568px;background:linear-gradient(180deg,#6f7c90 0%,#b9b8b6 40%,#5d7b9a 65%,#6f9a4c 82%,#55803a 100%)}
.divider{position:absolute;left:483px;top:0;width:3px;height:568px;background:var(--orange)}
.side-band{position:absolute;top:0;height:568px;width:146px;display:flex;align-items:center;justify-content:center}
.side-band--left{left:0;background:var(--teal-soft)}
.side-band--right{right:0;background:var(--navy-soft)}
.side-title{writing-mode:vertical-rl;font-weight:700;font-size:37px;letter-spacing:3px;white-space:nowrap}
.side-band--left .side-title{transform:rotate(180deg);color:var(--white)}
.side-band--right .side-title{color:#a9dcd8}
.backdrop .brand{left:158px;top:18px}
.tagline-box{position:absolute;background:var(--teal-soft);font-weight:600;line-height:.95}
.backdrop .tagline-box{left:148px;top:431px;width:275px;height:94px;padding:12px 0 0 22px;font-size:39px}
.closing-box{position:absolute;background:var(--navy-soft);display:flex;align-items:center;justify-content:flex-end;text-align:right;font-weight:600;letter-spacing:2px;line-height:1.1}
.backdrop .closing-box{left:522px;top:313px;width:325px;height:101px;padding-right:116px;font-size:24px}

/* Countertop */
.counter{left:17px;top:608px;width:432px;height:202px;background:var(--navy);border-top:3px solid var(--orange);box-shadow:0 1px 3px rgba(0,0,0,.3)}
.counter .brand{position:absolute;left:126px;top:28px}
.services{list-style:none;font-weight:500;text-align:center;line-height:1.4}
.counter .services{position:absolute;left:0;right:0;top:103px;font-size:17px}

/* Retractable banner */
.banner{left:764px;top:608px;width:246px;height:579px;box-shadow:0 1px 3px rgba(0,0,0,.3);background:var(--navy);overflow:hidden}
.banner-head{position:absolute;left:0;top:0;width:246px;height:110px;background:var(--navy);border-bottom:3px solid var(--white)}
.banner-head .brand{position:absolute;left:14px;top:22px}
.photo-deal{left:0;top:113px;width:246px;height:213px;background:linear-gradient(150deg,#d8c7ad,#b78f6a 45%,#6f6a6b 75%,#3c4046)}
.photo-house{left:0;top:330px;width:246px;height:249px;background:linear-gradient(180deg,#d8e4ea 0%,#9fae9c 35%,#b8b8ae 60%,#4f7a3a 100%)}
.banner-rule{position:absolute;left:0;top:326px;width:246px;height:4px;background:var(--orange)}
.banner .closing-box{left:61px;top:124px;width:185px;height:53px;padding-right:72px;font-size:13px;letter-spacing:1.2px;background:rgba(70,70,70,.85)}
.banner .tagline-box{left:0;top:249px;width:157px;height:50px;padding:6px 0 0 23px;font-size:19px}
.banner .services{position:absolute;right:0;top:437px;width:164px;padding:6px 8px 6px 0;text-align:right;font-size:12.5px;background:var(--teal-soft);line-height:1.35}

/* Standalone logo */
.logo-lockup{left:215px;top:960px}
.logo-lockup .brand-mark{background:var(--teal)}
.logo-lockup .brand-name{color:var(--navy)}
</style>
</head>
<body>

<section class="abs backdrop" aria-label="Backdrop display">
  <div class="photo photo-handshake" role="img" aria-label="Photo: smiling builder shaking hands on a construction site"></div>
  <div class="photo photo-family" role="img" aria-label="Photo: family standing in front of their new home"></div>
  <div class="divider"></div>
  <div class="side-band side-band--left"><span class="side-title">HARD MONEY LENDING</span></div>
  <div class="side-band side-band--right"><span class="side-title">HARD MONEY LENDING</span></div>
  <div class="abs brand">
    <span class="brand-mark" style="width:18px;height:18px"></span>
    <span class="brand-name" style="font-size:18px">Crestmoor<br>Funding<br>Partners LLC</span>
  </div>
  <div class="tagline-box">Hard Money<br>Lending</div>
  <div class="closing-box"><span>QUICK,<br>HASSLE-FREE<br>CLOSINGS</span></div>
</section>
<div class="label" style="left:570px;top:608px">Backdrop</div>

<section class="abs counter" aria-label="Countertop wrap">
  <div class="brand">
    <span class="brand-mark" style="width:16px;height:16px"></span>
    <span class="brand-name" style="font-size:15px">Crestmoor<br>Funding<br>Partners LLC</span>
  </div>
  <ul class="services"><li>· Fix &amp; Flip</li><li>· New Construction</li><li>· Cash Out Refinance</li></ul>
</section>
<div class="label" style="left:311px;top:836px">Countertop Wrap</div>

<section class="abs banner" aria-label="Retractable banner">
  <div class="banner-head">
    <div class="brand">
      <span class="brand-mark" style="width:18px;height:18px"></span>
      <span class="brand-name" style="font-size:17px">Crestmoor<br>Funding<br>Partners LLC</span>
    </div>
  </div>
  <div class="photo photo-deal" role="img" aria-label="Photo: builder and client shaking hands"></div>
  <div class="banner-rule"></div>
  <div class="photo photo-house" role="img" aria-label="Photo: two-storey suburban house"></div>
  <div class="closing-box"><span>QUICK,<br>HASSLE-FREE<br>CLOSINGS</span></div>
  <div class="tagline-box">Hard Money<br>Lending</div>
  <ul class="services"><li>· Fix &amp; Flip</li><li>· New Construction</li><li>· Cash Out Refinance</li></ul>
</section>
<div class="label" style="left:588px;top:1166px">Retractable Banner</div>

<div class="abs brand logo-lockup" style="gap:18px">
  <span class="brand-mark" style="width:40px;height:40px"></span>
  <span class="brand-name" style="font-size:34px;line-height:1.3">Crestmoor<br>Funding<br>Partners LLC</span>
</div>

</body>
</html>
```